Business Card Design

We need a new business card design for a company based in Corvane, CO. We provide business consulting services in the information technology / services space. We like variations of the color blue, aqua, black, light tan, and white. Would like "cool" tones. The design should clearly communicate professionalism. Think outside the box - we don't want something "typical". Our company name is "Vantrell Advisory, LLC".
Updates

Thank you all for your submissions. We have seen some very creative and inspired designs. We have made a decision and will be moving forward with that design. Appreciate all of the hard work.

Industry/Entity Type

Information Technology

Contact Information for Business Card

Denise Harlow Trumbey
482 West Maple Ridge Dr.
Corvane, CO 76185

```html
<!DOCTYPE html>
<html lang="en">
<head>
<meta charset="utf-8">
<title>Vantrell Advisory – Business Cards</title>
<link rel="stylesheet" href="https://fonts.googleapis.com/css2?family=Open+Sans:wght@400;600&display=swap">
<style>
  :root {
    --backdrop: #eef0f2;
    --paper: #ffffff;
    --ink: #2b2b2b;
    --ink-soft: #5a5a5a;
    --accent-red: #e0353b;
    --accent-blue: #3b8fd4;
  }
  * { box-sizing: border-box; margin: 0; padding: 0; }
  html, body { width: 1200px; height: 828px; overflow: hidden; }
  body {
    background: var(--backdrop);
    font-family: "Open Sans", Arial, sans-serif;
    position: relative;
  }
  .card {
    position: absolute;
    top: 260px;
    width: 540px;
    height: 309px;
    background: var(--paper);
    box-shadow: 0 2px 10px rgba(0,0,0,0.08);
    color: var(--ink);
  }
  .card--red { left: 40px; --accent: var(--accent-red); }
  .card--blue { left: 620px; --accent: var(--accent-blue); }

  .card__marker {
    position: absolute; left: 0; top: 168px;
    width: 24px; height: 50px;
    background: var(--accent);
  }
  .card__person { position: absolute; left: 38px; top: 170px; }
  .card__name { font-size: 17px; font-weight: 400; line-height: 22px; white-space: nowrap; }
  .card__role { font-size: 12.5px; color: var(--accent); line-height: 18px; white-space: nowrap; }

  .card__company { position: absolute; right: 62px; top: 34px; text-align: right; }
  .card__brand { font-size: 19px; font-weight: 600; color: var(--accent); line-height: 24px; white-space: nowrap; }
  .card__tagline { font-size: 12px; color: var(--ink-soft); line-height: 17px; letter-spacing: 0.2px; white-space: nowrap; }

  .card__rule {
    position: absolute; left: 250px; right: 58px; top: 88px;
    height: 1px; background: var(--accent);
  }

  .card__contacts {
    position: absolute; right: 64px; top: 100px;
    list-style: none; text-align: right;
    font-size: 10.5px; color: var(--ink-soft); line-height: 20px;
    white-space: nowrap;
  }

  .card__icons {
    position: absolute; right: 26px; top: 94px;
    display: flex; flex-direction: column; align-items: center; gap: 4px;
  }
  .icon-badge {
    width: 26px; padding: 4px 0;
    background: var(--accent); border-radius: 4px;
    display: flex; flex-direction: column; align-items: center; gap: 4px;
  }
  .icon-badge svg { width: 14px; height: 14px; fill: #fff; }
  .icon-plain { width: 14px; height: 14px; fill: var(--accent); }
</style>
</head>
<body>

<article class="card card--red">
  <div class="card__company">
    <div class="card__brand">Vantrell Advisory, LLC</div>
    <div class="card__tagline">Business Consulting Services</div>
  </div>
  <div class="card__rule"></div>
  <ul class="card__contacts">
    <li>+11 11 2 903 415</li>
    <li>+11 11 2 903 416</li>
    <li>www.vantrelladv.com</li>
    <li>dharlow@vantrelladv.com</li>
    <li>482 West Maple Ridge Dr. Corvane, CO 76185</li>
  </ul>
  <div class="card__icons">
    <div class="icon-badge">
      <svg viewBox="0 0 24 24" aria-hidden="true"><path d="M6.6 10.8a15.1 15.1 0 0 0 6.6 6.6l2.2-2.2a1 1 0 0 1 1-.25 11.4 11.4 0 0 0 3.6.57 1 1 0 0 1 1 1V20a1 1 0 0 1-1 1A17 17 0 0 1 3 4a1 1 0 0 1 1-1h3.5a1 1 0 0 1 1 1c0 1.25.2 2.45.57 3.57a1 1 0 0 1-.25 1z"/></svg>
      <svg viewBox="0 0 24 24" aria-hidden="true"><path d="M7 2h10a1 1 0 0 1 1 1v18a1 1 0 0 1-1 1H7a1 1 0 0 1-1-1V3a1 1 0 0 1 1-1zm1 3v12h8V5zm4 13.5a1 1 0 1 0 0 2 1 1 0 0 0 0-2z"/></svg>
      <svg viewBox="0 0 24 24" aria-hidden="true"><path d="M12 2a10 10 0 1 0 0 20 10 10 0 0 0 0-20zm6.9 6h-3a15 15 0 0 0-1.3-3.9A8 8 0 0 1 18.9 8zM12 4c.8 1.2 1.5 2.5 1.9 4h-3.8c.4-1.5 1.1-2.8 1.9-4zM4.3 14a8 8 0 0 1 0-4h3.4a16 16 0 0 0 0 4zm.8 2h3a15 15 0 0 0 1.3 3.9A8 8 0 0 1 5.1 16zm3-8h-3a8 8 0 0 1 4.3-3.9A15 15 0 0 0 8.1 8zM12 20c-.8-1.2-1.5-2.5-1.9-4h3.8c-.4 1.5-1.1 2.8-1.9 4zm2.3-6H9.7a14 14 0 0 1 0-4h4.6a14 14 0 0 1 0 4zm.3 5.9a15 15 0 0 0 1.3-3.9h3a8 8 0 0 1-4.3 3.9zm1.7-5.9a16 16 0 0 0 0-4h3.4a8 8 0 0 1 0 4z"/></svg>
    </div>
    <svg class="icon-plain" viewBox="0 0 24 24" aria-hidden="true"><path d="M3 5h18a1 1 0 0 1 1 1v12a1 1 0 0 1-1 1H3a1 1 0 0 1-1-1V6a1 1 0 0 1 1-1zm1 2.4V17h16V7.4l-8 5.3z M4.6 7h14.8L12 11.9z"/></svg>
    <svg class="icon-plain" viewBox="0 0 24 24" aria-hidden="true"><path d="M12 2a7 7 0 0 0-7 7c0 5.2 7 13 7 13s7-7.8 7-13a7 7 0 0 0-7-7zm0 9.5A2.5 2.5 0 1 1 12 6.5a2.5 2.5 0 0 1 0 5z"/></svg>
  </div>
  <div class="card__marker"></div>
  <div class="card__person">
    <div class="card__name">Denise Harlow Trumbey</div>
    <div class="card__role">Consultant &amp; Manager</div>
  </div>
</article>

<article class="card card--blue">
  <div class="card__company">
    <div class="card__brand">Vantrell Advisory, LLC</div>
    <div class="card__tagline">Business Consulting Services</div>
  </div>
  <div class="card__rule"></div>
  <ul class="card__contacts">
    <li>+11 11 2 903 415</li>
    <li>+11 11 2 903 416</li>
    <li>www.vantrelladv.com</li>
    <li>dharlow@vantrelladv.com</li>
    <li>482 West Maple Ridge Dr. Corvane, CO 76185</li>
  </ul>
  <div class="card__icons">
    <div class="icon-badge">
      <svg viewBox="0 0 24 24" aria-hidden="true"><path d="M6.6 10.8a15.1 15.1 0 0 0 6.6 6.6l2.2-2.2a1 1 0 0 1 1-.25 11.4 11.4 0 0 0 3.6.57 1 1 0 0 1 1 1V20a1 1 0 0 1-1 1A17 17 0 0 1 3 4a1 1 0 0 1 1-1h3.5a1 1 0 0 1 1 1c0 1.25.2 2.45.57 3.57a1 1 0 0 1-.25 1z"/></svg>
      <svg viewBox="0 0 24 24" aria-hidden="true"><path d="M7 2h10a1 1 0 0 1 1 1v18a1 1 0 0 1-1 1H7a1 1 0 0 1-1-1V3a1 1 0 0 1 1-1zm1 3v12h8V5zm4 13.5a1 1 0 1 0 0 2 1 1 0 0 0 0-2z"/></svg>
      <svg viewBox="0 0 24 24" aria-hidden="true"><path d="M12 2a10 10 0 1 0 0 20 10 10 0 0 0 0-20zm6.9 6h-3a15 15 0 0 0-1.3-3.9A8 8 0 0 1 18.9 8zM12 4c.8 1.2 1.5 2.5 1.9 4h-3.8c.4-1.5 1.1-2.8 1.9-4zM4.3 14a8 8 0 0 1 0-4h3.4a16 16 0 0 0 0 4zm.8 2h3a15 15 0 0 0 1.3 3.9A8 8 0 0 1 5.1 16zm3-8h-3a8 8 0 0 1 4.3-3.9A15 15 0 0 0 8.1 8zM12 20c-.8-1.2-1.5-2.5-1.9-4h3.8c-.4 1.5-1.1 2.8-1.9 4zm2.3-6H9.7a14 14 0 0 1 0-4h4.6a14 14 0 0 1 0 4zm.3 5.9a15 15 0 0 0 1.3-3.9h3a8 8 0 0 1-4.3 3.9zm1.7-5.9a16 16 0 0 0 0-4h3.4a8 8 0 0 1 0 4z"/></svg>
    </div>
    <svg class="icon-plain" viewBox="0 0 24 24" aria-hidden="true"><path d="M3 5h18a1 1 0 0 1 1 1v12a1 1 0 0 1-1 1H3a1 1 0 0 1-1-1V6a1 1 0 0 1 1-1zm1 2.4V17h16V7.4l-8 5.3z M4.6 7h14.8L12 11.9z"/></svg>
    <svg class="icon-plain" viewBox="0 0 24 24" aria-hidden="true"><path d="M12 2a7 7 0 0 0-7 7c0 5.2 7 13 7 13s7-7.8 7-13a7 7 0 0 0-7-7zm0 9.5A2.5 2.5 0 1 1 12 6.5a2.5 2.5 0 0 1 0 5z"/></svg>
  </div>
  <div class="card__marker"></div>
  <div class="card__person">
    <div class="card__name">Denise Harlow Trumbey</div>
    <div class="card__role">Consultant &amp; Manager</div>
  </div>
</article>

</body>
</html>
```